Bamboo & Ember Business Card FUN & EXCITING

Here is the Information for the Card:
Harpreet Kalra (Toby)
E: TobyKalra@mailbox-demo.com
C: (480) 555-0147
www.BambooEmberLV.com

We don't want traditional Indian cliche, We a playful bold and fun business card.

Files: https://files.sharebox-demo.net/folders/7QtpLmzR2xVbN4kHs9wYcDfJ3eGaUoPi

https://files.sharebox-demo.net/folders/5ZrqTwyX8mKcE2vBn6aLpHsQ9uFjRgOe

Target Market(s)

Las Vegas Local Restaurant

Industry/Entity Type

Indian Restaurant

Contact Information for Business Card

Name, Email, Cell Phone, Company Logo

```html
<!DOCTYPE html>
<html lang="en">
<head>
<meta charset="UTF-8">
<title>Bamboo &amp; Ember – Business Card</title>
<link rel="stylesheet" href="https://fonts.googleapis.com/css2?family=Open+Sans:wght@400;700;800&family=Playfair+Display:ital@1&display=swap">
<style>
  :root {
    --stage: #1f1f21;
    --card-dark: #141414;
    --card-light: #ffffff;
    --pink: #e4235e;
    --teal: #1fae95;
    --ink: #111111;
    --text-light: #e9e9e9;
    --mascot-cream: #efe6cf;
    --mascot-orange: #f08a2c;
  }
  * { box-sizing: border-box; margin: 0; padding: 0; }
  html, body {
    width: 1200px; height: 1029px; overflow: hidden;
    background: var(--stage);
    font-family: "Open Sans", Arial, sans-serif;
  }
  .stage {
    width: 1200px; height: 1029px;
    display: flex; flex-direction: column; align-items: center; justify-content: center;
    gap: 60px;
  }
  .card {
    position: relative;
    width: 700px; height: 400px;
    box-shadow: 0 20px 40px rgba(0,0,0,.45);
  }
  /* Front: contact side */
  .card--contact { background: var(--card-dark); color: var(--text-light); }
  .brand-name {
    position: absolute; top: 48px; right: 48px;
    font-weight: 800; font-size: 34px; letter-spacing: .5px;
    color: var(--pink); text-transform: uppercase;
  }
  .person { position: absolute; left: 48px; bottom: 48px; }
  .person__name { font-weight: 700; font-size: 30px; line-height: 1.1; }
  .person__first { color: var(--pink); }
  .person__last { color: var(--teal); }
  .person__nick { font-size: 17px; color: var(--text-light); margin: 2px 0 18px; }
  .contact-list { list-style: none; font-size: 19px; line-height: 1.5; }
  .contact-list li { display: flex; align-items: center; gap: 10px; }
  .contact-list svg { width: 16px; height: 16px; flex: none; }
  /* Back: logo side */
  .card--brand { background: var(--card-light); }
  .brand-lockup {
    position: absolute; inset: 0;
    display: flex; align-items: center; justify-content: center; gap: 28px;
  }
  .brand-lockup__text { text-align: left; }
  .brand-lockup__name {
    font-weight: 800; font-size: 52px; line-height: 1; color: var(--ink);
    text-transform: uppercase;
  }
  .brand-lockup__tagline {
    margin-top: 14px;
    font-family: "Playfair Display", Georgia, serif; font-style: italic;
    font-size: 18px; color: var(--ink);
  }
  .mascot {
    width: 190px; height: 200px; border-radius: 12px;
    background: linear-gradient(160deg, var(--mascot-cream) 0%, #f6dcc0 55%, var(--mascot-orange) 100%);
  }
</style>
</head>
<body>
  <main class="stage">
    <section class="card card--contact">
      <div class="brand-name">Bamboo &amp; Ember</div>
      <div class="person">
        <p class="person__name"><span class="person__first">Harpreet</span> <span class="person__last">Kalra</span></p>
        <p class="person__nick">(Toby)</p>
        <ul class="contact-list">
          <li>
            <svg viewBox="0 0 16 16" aria-hidden="true"><path fill="#e4235e" d="M3.5 1.5l2.5 0 1 3.5-1.7 1.2a8 8 0 0 0 4.5 4.5L11 9l3.5 1v2.5c0 1-1 2-2 2A11 11 0 0 1 1.5 3.5c0-1 1-2 2-2z"/></svg>
            (480) 555-0147
          </li>
          <li>
            <svg viewBox="0 0 16 16" aria-hidden="true"><rect x="1" y="3" width="14" height="10" rx="1.5" fill="#e4235e"/><path d="M1.5 4l6.5 5 6.5-5" stroke="#141414" stroke-width="1.4" fill="none"/></svg>
            TobyKalra@mailbox-demo.com
          </li>
          <li>
            <svg viewBox="0 0 16 16" aria-hidden="true"><circle cx="8" cy="8" r="7" fill="#e4235e"/><path d="M1 8h14M8 1c-3 3.5-3 10.5 0 14M8 1c3 3.5 3 10.5 0 14" stroke="#141414" stroke-width="1.1" fill="none"/></svg>
            www.BambooEmberLV.com
          </li>
        </ul>
      </div>
    </section>

    <section class="card card--brand">
      <div class="brand-lockup">
        <div class="brand-lockup__text">
          <p class="brand-lockup__name">Bamboo<br>&amp; Ember</p>
          <p class="brand-lockup__tagline">“A match made in heaven”</p>
        </div>
        <div class="mascot" role="img" aria-label="Cartoon mascots: a walking flatbread and a curry bowl with hearts and sparkles"></div>
      </div>
    </section>
  </main>
</body>
</html>
```